4 'Thank you' greetings cards designs

We are a small greetings card publisher and we need designs for a range of 'Thank you' greetings cards and notecards.
This project is for a total of 4 designs.
Please take a look at this board on Moodpinly, to see the kind of thing we are looking for: https://www.moodpinly.example/dorvek481/thank-you-cards/
The cards will be printed at a maximum size of 131mm x 183mm (including a 3mm bleed) so please provide 300dpi CMYK files at this size. Please ensure that any text (or elements of the design that are not part of the bleed) are at least 11mm in from each edge. Also, please note that cards do not have to have a bleed if your design doesn't require it (e.g. a plain white background).
Please provide 2 designs in 'portrait' orientation and 2 in 'landscape'.
Please provide 2 designs that just have the words 'Thank you' and then 2 designs that include your choice of these alternative messages:
Thank you so much
Thanks very much
Thank you very much
Thanks a million
Just to say thank you
A big thank you
A really big thank you
Feel free to use an exclamation mark on a couple of your designs, if you wish!
Other than the above guidelines, everything else is up to you in terms of colours, fonts, shapes, etc. - but please use the Moodpinly board to see the kind of designs we are looking for.
Thank you!

```html
<!DOCTYPE html>
<html lang="en">
<head>
<meta charset="utf-8">
<title>Thank You Greeting Cards</title>
<link rel="stylesheet" href="https://fonts.googleapis.com/css2?family=Allura&family=Caveat+Brush&display=swap">
<style>
  :root {
    --plum: #4f2772;
    --paper: #ffffff;
    --magenta: #ec1e7a;
    --pink: #ee3f96;
    --pink-shadow: #c42a78;
    --teal-light: #bfe8e2;
    --teal: #5cc3b6;
    --teal-deep: #1f9a8c;
    --gold: #fbbf4b;
    --violet: #8e4fa0;
    --red: #e8253d;
  }
  html, body {
    margin: 0;
    padding: 0;
    width: 1200px;
    height: 805px;
    overflow: hidden;
    background: var(--plum);
  }
  .canvas {
    position: relative;
    width: 1200px;
    height: 805px;
    background: var(--plum);
  }
  .card {
    position: absolute;
    top: 26px;
    width: 540px;
    height: 752px;
    background: var(--paper);
  }
  .card--fabric { left: 22px; }
  .card--circle { left: 638px; }
  .card svg {
    position: absolute;
    inset: 0;
    width: 540px;
    height: 752px;
  }
  .script-greeting {
    font-family: "Allura", cursive;
    font-size: 92px;
    fill: var(--magenta);
    stroke: var(--paper);
    stroke-width: 7px;
    paint-order: stroke fill;
    stroke-linejoin: round;
  }
  .brush-greeting {
    font-family: "Caveat Brush", cursive;
    font-size: 96px;
    fill: var(--paper);
  }
  .brush-greeting--shadow { fill: var(--pink-shadow); }
</style>
</head>
<body>
<main class="canvas">

  <section class="card card--fabric">
    <svg viewBox="0 0 540 752" xmlns="http://www.w3.org/2000/svg">
      <defs>
        <radialGradient id="fabric-tone" cx="50%" cy="50%" r="60%">
          <stop offset="0" stop-color="var(--teal-light)"/>
          <stop offset="0.6" stop-color="var(--teal)"/>
          <stop offset="1" stop-color="var(--teal-deep)"/>
        </radialGradient>
      </defs>
      <g class="fabric-frame" transform="translate(-22 -26)">
        <path class="fabric-frame__border"
          d="M82 226 Q84 172 112 146 Q140 120 195 116 Q250 112 281 142 Q312 172 348 150 Q384 128 416 120 Q448 112 484 156 Q520 200 536 276 Q552 352 536 384 Q520 416 536 456 Q552 496 532 552 Q512 608 504 620 Q496 632 448 656 Q400 680 396 660 Q392 640 256 636 Q120 632 96 620 Q72 608 66 560 Q60 512 66 444 Q72 376 52 344 Q32 312 56 296 Q80 280 82 226 Z"
          fill="none" stroke="var(--magenta)" stroke-width="26" stroke-linejoin="round"/>
        <path class="fabric-frame__pattern" role="img" aria-label="Teal wavy line pattern gathered like draped fabric"
          d="M82 226 Q84 172 112 146 Q140 120 195 116 Q250 112 281 142 Q312 172 348 150 Q384 128 416 120 Q448 112 484 156 Q520 200 536 276 Q552 352 536 384 Q520 416 536 456 Q552 496 532 552 Q512 608 504 620 Q496 632 448 656 Q400 680 396 660 Q392 640 256 636 Q120 632 96 620 Q72 608 66 560 Q60 512 66 444 Q72 376 52 344 Q32 312 56 296 Q80 280 82 226 Z"
          fill="url(#fabric-tone)" stroke="var(--paper)" stroke-width="9" stroke-linejoin="round"/>
        <path class="fabric-frame__stitch"
          d="M82 226 Q84 172 112 146 Q140 120 195 116 Q250 112 281 142 Q312 172 348 150 Q384 128 416 120 Q448 112 484 156 Q520 200 536 276 Q552 352 536 384 Q520 416 536 456 Q552 496 532 552 Q512 608 504 620 Q496 632 448 656 Q400 680 396 660 Q392 640 256 636 Q120 632 96 620 Q72 608 66 560 Q60 512 66 444 Q72 376 52 344 Q32 312 56 296 Q80 280 82 226 Z"
          fill="none" stroke="#6b3a5c" stroke-width="2" stroke-dasharray="8 5"/>
        <text class="script-greeting" x="290" y="416" text-anchor="middle">Thank You</text>
      </g>
    </svg>
  </section>

  <section class="card card--circle">
    <svg viewBox="0 0 540 752" xmlns="http://www.w3.org/2000/svg">
      <defs>
        <radialGradient id="badge-shadow" cx="50%" cy="50%" r="50%">
          <stop offset="0" stop-color="#000" stop-opacity="0.14"/>
          <stop offset="1" stop-color="#000" stop-opacity="0"/>
        </radialGradient>
      </defs>
      <g class="badge" transform="translate(-638 -26)">
        <ellipse class="badge__shadow" cx="880" cy="574" rx="170" ry="16" fill="url(#badge-shadow)"/>
        <circle class="badge__disc" cx="862" cy="388" r="182" fill="var(--pink)"/>

        <g class="badge__message" text-anchor="middle">
          <text class="brush-greeting brush-greeting--shadow" x="875" y="378">Thank U</text>
          <text class="brush-greeting" x="870" y="372">Thank U</text>
          <text class="brush-greeting brush-greeting--shadow" x="875" y="466">very much</text>
          <text class="brush-greeting" x="870" y="460">very much</text>
        </g>

        <g class="confetti">
          <rect x="1061" y="329" width="9" height="9" fill="var(--red)"/>
          <polygon points="1070,378 1100,386 1086,398" fill="var(--gold)"/>
          <polygon points="1062,434 1122,414 1112,468" fill="var(--pink)"/>
          <rect x="1132" y="448" width="12" height="12" fill="var(--violet)" transform="rotate(45 1138 454)"/>
          <polygon points="1074,472 1102,502 1080,502" fill="var(--gold)"/>
          <circle cx="757" cy="533" r="14" fill="var(--gold)"/>
          <circle cx="685" cy="526" r="5" fill="var(--violet)"/>
          <circle cx="701" cy="550" r="4" fill="var(--gold)"/>
          <circle cx="724" cy="555" r="5" fill="var(--pink)"/>
          <circle cx="707" cy="593" r="5" fill="var(--violet)"/>
          <circle cx="746" cy="582" r="5" fill="var(--pink)"/>
        </g>
      </g>
    </svg>
  </section>

</main>
</body>
</html>
```